R. Calloway Peril Counsel Business Card

I need a business card that incorporates a two divisions of my company into one business card. The main company or division is R. Calloway Peril Counsel. We have a secondary division of R. Calloway Peril Counsel call Calloway Freight Insurance. I would like this name to be listed as "A Division of R. Calloway Peril Counsel".

Target Market(s)

Customers looking for insurance for their business. WE target businesses with revenues over $5MM

Industry/Entity Type

Business Insurance

Contact Information for Business Card

Use the current logo, but make the R. Calloway Peril Counsel most prevelant over the Calloway Freight Insurance. Name, email, phone number and location

Colors
0054AA
0677BA
7BADD7
CADEEF
E8F1F8

Requirements
Must have
• my current logo
Nice to have
• would like to have "A Division of R. Calloway Peril Counsel" on the card

```html
<!DOCTYPE html>
<html lang="en">
<head>
<meta charset="utf-8">
<title>R. Calloway Peril Counsel – Business Card</title>
<link href="https://fonts.googleapis.com/css2?family=Tinos:ital,wght@0,400;0,700;1,400&display=swap" rel="stylesheet">
<style>
  :root {
    --page: #3b3b3d;
    --card-navy: #1b1f55;
    --card-navy-deep: #13163f;
    --pattern-light: #3a3f96;
    --ink-white: #f2f3f8;
    --ink-grey: #9a9cae;
    --rule: #6d7092;
  }
  * { margin: 0; padding: 0; box-sizing: border-box; }
  html, body { width: 1200px; height: 875px; overflow: hidden; background: var(--page); }
  body { font-family: "Tinos", "Times New Roman", serif; color: var(--ink-white); position: relative; }

  .card {
    position: absolute; left: 250px; width: 700px; height: 400px;
    border-radius: 22px; overflow: hidden; background: var(--card-navy);
  }
  .card--front { top: 30px; }
  .card--back { top: 445px; }

  /* Front */
  .front-pattern {
    position: absolute; inset: 0;
    background: radial-gradient(ellipse at 42% 45%, var(--pattern-light) 0%, var(--card-navy) 45%, var(--card-navy-deep) 100%);
  }
  .front-mark {
    position: absolute; left: 50%; top: 50%; transform: translate(-50%, -50%);
    display: flex; align-items: center; gap: 14px;
    font-size: 22px; letter-spacing: 1px; color: var(--ink-white);
  }
  .mark-square { width: 30px; height: 30px; background: var(--ink-white); }

  /* Back */
  .brand-bar {
    position: absolute; left: 40px; right: 40px; top: 48px; height: 110px;
    display: flex; align-items: center; justify-content: center; gap: 22px;
    border-top: 1px solid var(--rule); border-bottom: 1px solid var(--rule);
  }
  .brand-main, .brand-division {
    font-size: 25px; line-height: 1.15; letter-spacing: 1.5px; text-transform: uppercase;
  }
  .brand-main { text-align: right; }
  .brand-square { width: 74px; height: 74px; background: var(--ink-white); flex: none; }
  .division-note { font-size: 12px; letter-spacing: 0.5px; text-transform: none; display: block; margin-top: 4px; }

  .person { position: absolute; left: 48px; top: 190px; }
  .person-name { font-size: 26px; font-weight: 700; color: var(--ink-grey); }
  .person-title { font-size: 18px; margin-top: 4px; }

  .contact-rule { position: absolute; left: 48px; width: 300px; top: 262px; border-top: 1px solid var(--rule); }

  .contact-list { position: absolute; left: 48px; top: 276px; list-style: none; }
  .contact-list li { display: flex; align-items: center; gap: 12px; font-size: 16px; height: 26px; white-space: nowrap; }
  .contact-list svg, .main-lines svg { width: 16px; height: 16px; flex: none; fill: var(--ink-grey); }

  .main-lines { position: absolute; right: 44px; top: 192px; list-style: none; }
  .main-lines li { display: flex; align-items: center; gap: 10px; font-size: 16px; height: 26px; }
  .main-lines em { font-style: italic; }
</style>
</head>
<body>

<section class="card card--front" aria-label="Card front">
  <div class="front-pattern" role="img" aria-label="Repeating embossed monogram tile pattern in navy and violet"></div>
  <div class="front-mark">
    <span class="mark-square"></span>
    <span>R. Calloway Peril Counsel</span>
  </div>
</section>

<section class="card card--back" aria-label="Card back">
  <header class="brand-bar">
    <div class="brand-main">R. Calloway<br>Peril Counsel</div>
    <span class="brand-square"></span>
    <div class="brand-division">Calloway<br>Freight Insurance
      <span class="division-note">A Division of R. Calloway Peril Counsel</span>
    </div>
  </header>

  <div class="person">
    <div class="person-name">Dale Brannick</div>
    <div class="person-title">Founder / CEO</div>
  </div>

  <ul class="main-lines">
    <li><svg viewBox="0 0 24 24"><path d="M6.6 10.8a15 15 0 0 0 6.6 6.6l2.2-2.2a1 1 0 0 1 1-.25 11.4 11.4 0 0 0 3.6.57 1 1 0 0 1 1 1V20a1 1 0 0 1-1 1A17 17 0 0 1 3 4a1 1 0 0 1 1-1h3.5a1 1 0 0 1 1 1c0 1.25.2 2.45.57 3.57a1 1 0 0 1-.25 1z"/></svg>770-555-0142 <em>R. Calloway Main</em></li>
    <li><svg viewBox="0 0 24 24"><path d="M6.6 10.8a15 15 0 0 0 6.6 6.6l2.2-2.2a1 1 0 0 1 1-.25 11.4 11.4 0 0 0 3.6.57 1 1 0 0 1 1 1V20a1 1 0 0 1-1 1A17 17 0 0 1 3 4a1 1 0 0 1 1-1h3.5a1 1 0 0 1 1 1c0 1.25.2 2.45.57 3.57a1 1 0 0 1-.25 1z"/></svg>770-555-0163 <em>Freight Main</em></li>
  </ul>

  <div class="contact-rule"></div>

  <ul class="contact-list">
    <li><svg viewBox="0 0 24 24"><path d="M7 2h10a2 2 0 0 1 2 2v16a2 2 0 0 1-2 2H7a2 2 0 0 1-2-2V4a2 2 0 0 1 2-2zm0 3v13h10V5zm5 14.2a1 1 0 1 0 0 .1z"/></svg>404-555-0187</li>
    <li><svg viewBox="0 0 24 24"><path d="M2 5h20v14H2zm2 2v.5l8 5.5 8-5.5V7l-8 5.5z"/></svg>Dale@RCallowayIns.com</li>
    <li><svg viewBox="0 0 24 24"><path d="M12 2a10 10 0 1 0 0 20 10 10 0 0 0 0-20zm0 2c1.3 1.5 2.2 3.6 2.4 6H9.6C9.8 7.6 10.7 5.5 12 4zM4.1 11h3.5c.1 2.4.8 4.6 1.9 6.3A8 8 0 0 1 4.1 11zm5.5 0h4.8c-.2 2.4-1.1 4.5-2.4 6-1.3-1.5-2.2-3.6-2.4-6zm6.8 0h3.5a8 8 0 0 1-5.4 6.3c1.1-1.7 1.8-3.9 1.9-6.3z"/></svg>www.RCallowayPerilCounsel.com | www.CallowayFreightInsurance.com</li>
    <li><svg viewBox="0 0 24 24"><path d="M12 2a7 7 0 0 0-7 7c0 5 7 13 7 13s7-8 7-13a7 7 0 0 0-7-7zm0 9.5a2.5 2.5 0 1 1 0-5 2.5 2.5 0 0 1 0 5z"/></svg>Millbrook, SC Office, TX Texas</li>
  </ul>
</section>

</body>
</html>
```